Business Card Design for Logistics Startup

Link to my logo source file -
https://www.filecrate-demo.net/sh/qx7vmp2lr9kdwta/BBTzY4_LQm8hRuPoKvxVc?dl=0

We want a statement in our business card!
I have go thru your portfolio, and invites 3 of you guys to design my business card as the previous designer cannot give me the feel.
Let me know if you want any information.
Thanks.

Target Market(s)

Transport and Logistics
: Shippers, Freight Forwarders and Carriers.

Industry/Entity Type

Business

Contact Information for Business Card

Our details;

Name: Marcus Lim
Designation: General Manager
Mobile: +65 93415062
Email: marcus.lim@korvanth.com
Address: 7 Jalan Merpati Rise
TRINOX Plaza #03-17
Singapore 612379

Name: Daniel Ho
Designation: Director
Mobile: +65 97264318
Email: daniel.ho@korvanth.com
TRINOX Plaza #03-17
Singapore 612379

Colors
f37122

Requirements
Must have
• Logo from my source file.
• Please included tagline: Transport and Logistics
• If you guy can think of a tagline - Using E and S, that will be perfect. Such as Excellence in Service..

```html
<!DOCTYPE html>
<html lang="en">
<head>
<meta charset="utf-8">
<title>Korvanth Business Card</title>
<link rel="stylesheet" href="https://fonts.googleapis.com/css2?family=Montserrat:wght@400;500&family=Source+Sans+3:wght@400&display=swap">
<style>
  :root {
    --brand-orange: #f37122;
    --card-orange-light: #f4ac66;
    --card-orange-dark: #e3812e;
    --bar-orange: #f29a3e;
    --ink-orange: #ee8a2c;
    --paper: #ffffff;
    --backdrop: #eceef0;
    --display-font: "Montserrat", sans-serif;
    --body-font: "Source Sans 3", sans-serif;
  }
  * { box-sizing: border-box; margin: 0; padding: 0; }
  html, body {
    width: 1200px;
    height: 800px;
    overflow: hidden;
    background: var(--backdrop);
  }
  .canvas {
    position: relative;
    width: 1200px;
    height: 800px;
    display: flex;
    align-items: center;
    justify-content: center;
    gap: 40px;
  }
  .card {
    position: relative;
    width: 540px;
    height: 309px;
    border-radius: 2px;
    box-shadow: 0 2px 10px rgba(0, 0, 0, 0.08);
    overflow: hidden;
  }

  /* Front side */
  .card-front {
    background: linear-gradient(135deg, var(--card-orange-light), var(--card-orange-dark));
  }
  .front-frame {
    position: absolute;
    inset: 16px;
    border: 1.5px solid rgba(255, 255, 255, 0.9);
  }
  .front-content {
    position: absolute;
    inset: 0;
    display: flex;
    flex-direction: column;
    align-items: center;
    justify-content: center;
    gap: 26px;
    color: var(--paper);
  }
  .front-brand {
    display: flex;
    align-items: center;
    gap: 14px;
  }
  .brand-square {
    width: 18px;
    height: 18px;
    border: 2px solid currentColor;
  }
  .front-brand .brand-name {
    font-family: var(--display-font);
    font-weight: 500;
    font-size: 22px;
    letter-spacing: 0.18em;
  }
  .tagline {
    font-family: var(--display-font);
    font-weight: 400;
    font-size: 13px;
    letter-spacing: 0.28em;
    text-transform: uppercase;
  }

  /* Back side */
  .card-back {
    background: var(--paper);
    color: var(--ink-orange);
  }
  .back-brand {
    position: absolute;
    left: 44px;
    top: 62px;
    display: flex;
    align-items: center;
    gap: 14px;
  }
  .back-brand .brand-name {
    font-family: var(--display-font);
    font-weight: 500;
    font-size: 20px;
    letter-spacing: 0.14em;
  }
  .person {
    position: absolute;
    left: 44px;
    top: 146px;
  }
  .person-name {
    font-family: var(--display-font);
    font-weight: 500;
    font-size: 21px;
    letter-spacing: 0.1em;
    text-transform: uppercase;
    line-height: 1;
  }
  .person-title {
    font-family: var(--display-font);
    font-weight: 400;
    font-size: 10px;
    letter-spacing: 0.18em;
    text-transform: uppercase;
    margin-top: 4px;
  }
  .accent-bar {
    position: absolute;
    left: 238px;
    right: 0;
    top: 146px;
    height: 24px;
    background: var(--bar-orange);
  }
  .contact-list {
    position: absolute;
    left: 44px;
    top: 210px;
    list-style: none;
    font-family: var(--body-font);
    font-size: 14.5px;
    letter-spacing: 0.02em;
  }
  .contact-item {
    display: flex;
    align-items: center;
    gap: 14px;
    height: 24px;
  }
  .contact-icon {
    width: 13px;
    height: 13px;
    flex: none;
    fill: none;
    stroke: var(--ink-orange);
  }
  .contact-icon.solid { fill: var(--ink-orange); stroke: none; }
</style>
</head>
<body>
  <main class="canvas">
    <section class="card card-front" aria-label="Business card front">
      <div class="front-frame"></div>
      <div class="front-content">
        <div class="front-brand">
          <span class="brand-square"></span>
          <span class="brand-name">KORVANTH</span>
        </div>
        <p class="tagline">Transport and Logistics</p>
      </div>
    </section>

    <section class="card card-back" aria-label="Business card back">
      <div class="back-brand">
        <span class="brand-square"></span>
        <span class="brand-name">KORVANTH</span>
      </div>

      <div class="person">
        <p class="person-name">Marcus Lim</p>
        <p class="person-title">General Manager</p>
      </div>
      <div class="accent-bar"></div>

      <ul class="contact-list">
        <li class="contact-item">
          <svg class="contact-icon" viewBox="0 0 13 13" aria-hidden="true">
            <rect x="3" y="0.75" width="7" height="11.5" rx="1.2" stroke-width="1.4"/>
            <line x1="5.5" y1="10" x2="7.5" y2="10" stroke-width="1.2"/>
          </svg>
          <span>+65 93415062</span>
        </li>
        <li class="contact-item">
          <svg class="contact-icon solid" viewBox="0 0 13 13" aria-hidden="true">
            <path d="M0.5 2.5h12v8h-12z"/>
            <path d="M0.8 2.8l5.7 4.4 5.7-4.4" fill="none" stroke="#ffffff" stroke-width="1"/>
          </svg>
          <span>marcus.lim@korvanth.com</span>
        </li>
        <li class="contact-item">
          <svg class="contact-icon solid" viewBox="0 0 13 13" aria-hidden="true">
            <path d="M6.5 0.5a4.3 4.3 0 0 0-4.3 4.3c0 3.2 4.3 7.7 4.3 7.7s4.3-4.5 4.3-7.7A4.3 4.3 0 0 0 6.5 0.5zm0 6a1.7 1.7 0 1 1 0-3.4 1.7 1.7 0 0 1 0 3.4z"/>
          </svg>
          <span>7 Jalan Merpati Rise, TRINOX Plaza #03-17, Singapore 612379</span>
        </li>
      </ul>
    </section>
  </main>
</body>
</html>
```